Holzdesign Firma sucht stilvolles Corporate Design
Zielgruppe
Ich stelle Utensilien aus Holz für die Küche her und verkaufe diese übers Internet. In erster Linie platzsparende Messerbretter aus Holz. Meine Zielgruppe ist jeder in Deutschland der eine Küche hat und dort kocht.
Aufgabenstellung
Das Design sollte eher schlicht und innovativ wirken. Der Name WALDFUGE muss mit ihm Logo sein. Im Logo sollte auch eine Verbindung zum Holz erkennbar sein, am besten mit einem Holzbalken oder einem Baumstamm. Im Logo sollen keine Weihnachtsbäume oder ganze Bäume sichtbar sein. Die Farbwahl würde ich auf Farben die zu Holz und Natur passen eingrenzen.
Mit dem Design will ich mich von den übrigen Handwerksbetrieben abheben und nicht einfach die üblichen Standarddesigns kopieren.

```html
<!DOCTYPE html>
<html lang="de">
<head>
<meta charset="utf-8">
<title>WALDFUGE – Geschäftsausstattung</title>
<link href="https://fonts.googleapis.com/css2?family=Poppins:wght@300;400;500;600&display=swap" rel="stylesheet">
<style>
  :root{
    --bg:#f1f1f1;
    --paper:#ffffff;
    --ink:#333333;
    --ink-soft:#555555;
    --label:#8a8a8a;
    --wood-light:#ececec;
    --wood-mid:#d2d2d2;
    --wood-dark:#bdbdbd;
    --window:#a9a9a9;
    --shadow:0 6px 14px rgba(0,0,0,.22);
  }
  *{margin:0;padding:0;box-sizing:border-box}
  html,body{width:1200px;height:801px;overflow:hidden}
  body{
    position:relative;
    background:radial-gradient(ellipse at 40% 30%, #ffffff 0%, var(--bg) 70%, #e6e6e6 100%);
    font-family:"Poppins",sans-serif;
    font-weight:300;
    color:var(--ink);
  }
  .wood{
    background:linear-gradient(180deg,var(--wood-light) 0%,var(--wood-mid) 18%,#e6e6e6 34%,var(--wood-dark) 48%,#e9e9e9 62%,var(--wood-mid) 80%,var(--wood-light) 100%);
  }
  .piece{position:absolute;background:var(--paper);box-shadow:var(--shadow);overflow:hidden}

  /* brand block */
  .brand{position:absolute;display:flex;align-items:center;color:var(--ink)}
  .brand__square{border:solid var(--ink);flex:none}
  .brand__text{display:flex;flex-direction:column;line-height:1}
  .brand__name{font-weight:600;letter-spacing:.02em}
  .brand__slogan{font-weight:400;letter-spacing:.01em}

  .brand-strip{position:absolute;left:117px;top:103px;width:429px;height:89px}
  .brand--xl{left:20px;top:8px}
  .brand--xl .brand__square{width:68px;height:68px;border-width:4px;margin-right:8px}
  .brand--xl .brand__name{font-size:54px}
  .brand--xl .brand__slogan{font-size:18.5px;margin-top:2px}

  .brand--m .brand__square{width:28px;height:28px;border-width:2px;margin-right:4px}
  .brand--m .brand__name{font-size:22px}
  .brand--m .brand__slogan{font-size:7.6px}

  .brand--s .brand__square{width:22px;height:22px;border-width:1.6px;margin-right:3px}
  .brand--s .brand__name{font-size:17.5px}
  .brand--s .brand__slogan{font-size:6px}

  .label{position:absolute;top:264px;font-size:14px;color:var(--label);width:200px;text-align:center}

  /* business cards */
  .card{top:292px;width:260px;height:167px}
  .card--front{left:57px}
  .card--back{left:333px}
  .card--back .card__cut{position:absolute;inset:0}
  .card__name{position:absolute;left:130px;top:94px;font-size:9px;font-weight:500;letter-spacing:.04em}
  .card__role{position:absolute;left:130px;top:106px;font-size:6px;color:var(--ink-soft)}
  .card__info{position:absolute;top:125px;font-size:6.4px;line-height:9.6px;color:var(--ink-soft)}
  .card__info strong{font-weight:600;color:var(--ink)}

  /* envelope */
  .envelope{left:58px;top:496px;width:536px;height:267px}
  .envelope__logo{position:absolute;left:71px;top:36px;width:214px;height:44px}
  .envelope__window{position:absolute;left:47px;top:121px;width:206px;height:111px;border-radius:12px;background:linear-gradient(135deg,#b9b9b9,var(--window) 60%,#c4c4c4)}

  /* letterhead */
  .letter{left:630px;top:34px;width:520px;height:736px;font-size:6.4px;color:var(--ink-soft)}
  .letter__band{position:absolute;left:0;top:0;width:100%;height:117px}
  .letter__foot{position:absolute;left:0;bottom:0;width:100%;height:110px;clip-path:polygon(0 40%,100% 0,100% 100%,0 100%)}
  .letter__sender{position:absolute;left:62px;top:157px;font-size:4.6px}
  .letter__sender strong{font-weight:600;color:var(--ink)}
  .letter__recipient{position:absolute;left:62px;top:174px;font-size:7px;line-height:12.4px}
  .letter__contact{position:absolute;right:33px;top:134px;text-align:right;font-size:6px;line-height:10.4px}
  .letter__contact strong{font-weight:600;color:var(--ink)}
  .letter__fold{position:absolute;left:0;width:8px;height:1.4px;background:var(--ink)}
  .letter__body{position:absolute;left:62px;top:245px;width:420px;line-height:10.6px}
  .letter__body p{margin-bottom:10.4px}
  .letter__footer{position:absolute;top:691px;font-size:6px;line-height:10.4px}
  .letter__footer strong{font-weight:600;color:var(--ink)}
</style>
</head>
<body>

  <!-- primary brand block -->
  <div class="brand-strip wood" role="img" aria-label="Helle Holzmaserung als Hintergrund">
    <div class="brand brand--xl">
      <span class="brand__square"></span>
      <span class="brand__text">
        <span class="brand__name">WALDFUGE</span>
        <span class="brand__slogan">Hier könnte Ihr Slogan stehen.</span>
      </span>
    </div>
  </div>

  <div class="label" style="left:87px">Visitenkarte vorne</div>
  <div class="label" style="left:363px">Visitenkarte hinten</div>

  <!-- business card front -->
  <div class="piece card card--front wood" role="img" aria-label="Visitenkarte vorne mit Holzmaserung">
    <div class="brand brand--m" style="left:50px;top:67px">
      <span class="brand__square"></span>
      <span class="brand__text">
        <span class="brand__name">WALDFUGE</span>
        <span class="brand__slogan">Hier könnte Ihr Slogan stehen.</span>
      </span>
    </div>
  </div>

  <!-- business card back -->
  <div class="piece card card--back">
    <div class="card__cut wood" role="img" aria-label="Holzmaserung im oberen Kartenbereich" style="clip-path:polygon(0 0,100% 0,100% 38%,0 60.5%)"></div>
    <div class="brand brand--s" style="left:38px;top:29px">
      <span class="brand__square"></span>
      <span class="brand__text">
        <span class="brand__name">WALDFUGE</span>
        <span class="brand__slogan">Hier könnte Ihr Slogan stehen.</span>
      </span>
    </div>
    <div class="card__name">PAUL BEISPIEL</div>
    <div class="card__role">Position</div>
    <div class="card__info" style="left:38px"><strong>WALDFUGE</strong><br>Musterstraße 102<br>45868 Muster</div>
    <div class="card__info" style="left:130px"><br>p.beispiel@waldfuge.de<br>Tel.: 0231 470215<br>www.waldfuge.de</div>
  </div>

  <!-- envelope -->
  <div class="piece envelope">
    <div class="envelope__logo wood" role="img" aria-label="Holzmaserung hinter dem Markenzeichen">
      <div class="brand brand--s" style="left:10px;top:4px">
        <span class="brand__square" style="width:30px;height:30px"></span>
        <span class="brand__text">
          <span class="brand__name" style="font-size:24px">WALDFUGE</span>
          <span class="brand__slogan" style="font-size:8.6px">Hier könnte Ihr Slogan stehen.</span>
        </span>
      </div>
    </div>
    <div class="envelope__window"></div>
  </div>

  <!-- letterhead -->
  <div class="piece letter">
    <div class="letter__band wood" role="img" aria-label="Holzmaserung als Kopfband"></div>
    <div class="brand brand--s" style="left:332px;top:42px">
      <span class="brand__square"></span>
      <span class="brand__text">
        <span class="brand__name">WALDFUGE</span>
        <span class="brand__slogan">Hier könnte Ihr Slogan stehen.</span>
      </span>
    </div>

    <div class="letter__sender"><strong>WALDFUGE</strong> | Musterstraße 9 | 45868 Muster</div>
    <div class="letter__recipient">Herr Mustermann<br>Musterstraße 3<br>48555 Muster</div>
    <div class="letter__contact">
      <strong>WALDFUGE</strong><br>Musterstraße 93a<br>55555 Muster<br><br>
      Tel.: 0231 470215<br>Fax: 0231 470216<br>Mobil: 0170 5518342<br><br>
      info@waldfuge.de<br>www.waldfuge.de
    </div>

    <span class="letter__fold" style="top:261px"></span>
    <span class="letter__fold" style="top:367px"></span>
    <span class="letter__fold" style="top:520px"></span>

    <div class="letter__body">
      <p style="margin-bottom:21px">Hier steht eine Betreffzeile</p>
      <p>Sehr geehrte Frau Musterbeispiel,</p>
      <p>als Kunde unseres jungen und modernen Unternehmens erwartet<br>Sie Qualität in höchstem Maße.</p>
      <p>Sie können sicher zu sein, genau zu bekommen, was wir Ihnen versprechen.<br>Und damit werden Sie auch rundum zufrieden sein. Das garantieren wir Ihnen.</p>
      <p>Schauen Sie doch gleich das beiliegende Prospekt. Wir bieten Ihnen moderne und hochwertige Produkte, die auf dem neuesten Stand der Technik sind, an. Überzeugen Sie sich selbst von der hochwertigen Qualität unserer Produkte und bestellen Sie noch heute.</p>
      <p>Wir freuen uns auf Ihre Bestellung und sind bei Rückfragen gerne für Sie da.</p>
      <p>Mit freundlichen Grüßen</p>
    </div>

    <div class="letter__foot wood" role="img" aria-label="Holzmaserung als schräges Fußband"></div>
    <div class="letter__footer" style="left:49px"><strong>WALDFUGE</strong><br>Musterstraße 9<br>45868 Muster</div>
    <div class="letter__footer" style="left:188px">USt-IDNR: DE1234567<br>Steuernummer: 111/222/333<br>Inhaber: Paul Beispiel</div>
    <div class="letter__footer" style="left:364px">Stadtbank Musterstadt<br>IBAN: DE00 1234 0000 0000 5678<br>BIC: STBKDEXX00</div>
  </div>

</body>
</html>
```